Icecream Label Design [Merrows Crest]

Our company distributes ice cream in Japan. We produce a private brand that has always been know as Merrows.

However the brand design is poor and we have poor/almost zero brand recognition in the market. Currently people buy our product because it is made in NEW ZEALAND (quality) and represents very good value for money.

BUT

Going forward we want to market Merrows as a 'HIGH QUALITY' icecream BRAND in Japan. We need a package label that reflects this.

We are expanding the current product range (flavour and size) of our Merrow's icecream.

I think this is a great opportunity to get your design exposed in a large Asian market. We have very good distribution channels and will will sell a lot of this ice cream in Japan in the future and the Merrows brand/logo will become well recognized.

Really looking forward to seeing design proposals! Thank you, any questions please ask - PLT
Updates

Project Deadline Extended
Reason: Good morning all. Thank you for submissions. We are wishing to see more examples so have decided to extend the deadline. Looking forward to seeing your ideas. Thanks! Declan

Hi All,

I have sent through the current Merrow's logo. Please feel free to use this logo in your designs if you think it is appropriate. There is also an image of the current label for your reference - emphasis on fresh milk but the overall design is not good hence my request to you all...

Looking forward to your help and further submissions. 

Thanks!

Declan 

Project Deadline Extended
Reason: Just finalizing design. Have extended deadline to accommodate this. Your continued support and cooperation appreciated. Thanks! Declan

Project Deadline Extended
Reason: Finalizing decision being made. Thanks! Declan

Project Deadline Extended
Reason: Will make decision today. Thanks all! Declan

Project Deadline Extended

Target Market(s)

Mother's 30-55 (quality ingredients and value for money)

Industry/Entity Type

It Company

Requirements
Must have
• 1. The brand is Merrows Crest

2. You are designing a logo that will be used on our 1 litre tub and 500ML pottle. Design specification files are attached*.
*Please note: on both the 1L and 500ML tub space must be left for regulatory information. Image attached showing current regulatory information and and space on the 1L tub.

3. We want to use this logo/branding as a base for all our 4 flavour varieties noted below so the design must be able to accommodate this somehow.

4. Needs to have a text placeholder for Japanese translation. ie: if on the design you use text that says 'Vanilla Ice Cream' then somewhere there needs to be space for the Japanese equivalent バニラ アイスクリーム
Nice to have
• 1. Merrows uses 100% fresh milk and cream. It would be nice to convey this somehow.

2. Perhaps could include text 'Your Fresh Taste of New Zealand'

3. There are 4* flavour varieties.
Vanilla | Strawberry | Chocolate | Green Tea
* it would be nice to have a good Merrows base design/pattern which can then be modified slightly (image, colour etc maybe) to reflect each unique flavour.

```html
<!DOCTYPE html>
<html lang="en">
<head>
<meta charset="utf-8">
<title>Merrow's Ice Cream Labels</title>
<link rel="stylesheet" href="https://fonts.googleapis.com/css2?family=Open+Sans:wght@400;600;700&family=Noto+Sans+JP:wght@400&display=swap">
<style>
:root{
  --bg:#f2f2f2;
  --aqua:#7fd0d8;
  --aqua-line:#a9e0e5;
  --navy:#2b2f7c;
  --pink:#f4b7c6;
  --pink-line:#f9d3dc;
  --red:#e8262d;
  --orange:#f6a623;
  --black:#1a1a1a;
  --white:#ffffff;
  --milk:#eef6f8;
}
*{box-sizing:border-box;margin:0;padding:0}
html,body{width:1200px;height:1014px;overflow:hidden;background:var(--bg);font-family:"Open Sans",sans-serif}
.canvas{position:relative;width:1200px;height:1014px}
.label{position:absolute;overflow:hidden}
.label--vanilla{left:110px;top:120px;width:590px;height:780px;background:var(--aqua) repeating-linear-gradient(90deg,transparent 0 9px,var(--aqua-line) 9px 11px)}
.label--strawberry{left:795px;top:500px;width:320px;height:410px;background:var(--pink) repeating-linear-gradient(90deg,transparent 0 7px,var(--pink-line) 7px 9px)}
.lid{position:absolute;left:800px;top:40px;width:330px;height:330px;border-radius:50%;background:var(--aqua) repeating-linear-gradient(90deg,transparent 0 7px,var(--aqua-line) 7px 9px);overflow:hidden}
.seal{position:absolute}
.seal svg{width:100%;height:100%;display:block}
.milk-splash{position:absolute;left:0;right:0;bottom:0;background:linear-gradient(180deg,rgba(255,255,255,0) 0%,var(--milk) 22%,var(--white) 45%)}
.claim{position:absolute;font-weight:600;line-height:1.05;white-space:nowrap}
.claim__brand{font-weight:700}
.claim__pct{font-weight:700}
.nz-badge{position:absolute;border-radius:50%;background:var(--black);color:var(--white);display:flex;flex-direction:column;align-items:center;justify-content:center;text-align:center;font-weight:600;line-height:1.15;border:2px solid var(--white)}
.nz-badge__mark{border-radius:50%;background:#555;margin:3px 0}
</style>
</head>
<body>
<main class="canvas">

  <!-- Vanilla 500mL label -->
  <section class="label label--vanilla">
    <div class="milk-splash" role="img" aria-label="Splash of fresh milk" style="height:210px"></div>
    <div class="seal" style="left:60px;top:175px;width:470px;height:470px">
      <svg viewBox="0 0 400 400">
        <g fill="var(--navy)">
          <rect x="58.6" y="58.6" width="282.8" height="282.8"/>
          <rect x="58.6" y="58.6" width="282.8" height="282.8" transform="rotate(11.25 200 200)"/>
          <rect x="58.6" y="58.6" width="282.8" height="282.8" transform="rotate(22.5 200 200)"/>
          <rect x="58.6" y="58.6" width="282.8" height="282.8" transform="rotate(33.75 200 200)"/>
          <rect x="58.6" y="58.6" width="282.8" height="282.8" transform="rotate(45 200 200)"/>
          <rect x="58.6" y="58.6" width="282.8" height="282.8" transform="rotate(56.25 200 200)"/>
          <rect x="58.6" y="58.6" width="282.8" height="282.8" transform="rotate(67.5 200 200)"/>
          <rect x="58.6" y="58.6" width="282.8" height="282.8" transform="rotate(78.75 200 200)"/>
        </g>
        <circle cx="200" cy="200" r="165" fill="none" stroke="var(--white)" stroke-width="3"/>
        <defs>
          <path id="vTop" d="M50,200 A150,150 0 0 1 350,200"/>
          <path id="vBot" d="M60,200 A140,140 0 0 0 340,200"/>
          <path id="vMid" d="M75,212 Q200,165 325,212"/>
        </defs>
        <text font-family="Open Sans,sans-serif" font-weight="700" font-size="17" fill="var(--white)"><textPath href="#vTop" startOffset="50%" text-anchor="middle">Vanilla Ice Cream - 500mL</textPath></text>
        <text x="200" y="162" text-anchor="middle" font-family="Open Sans,sans-serif" font-weight="700" font-size="48" fill="var(--white)">Merrow's</text>
        <text font-family="Open Sans,sans-serif" font-weight="700" font-size="18" fill="var(--white)"><textPath href="#vMid" startOffset="50%" text-anchor="middle">High Quality Ice Cream</textPath></text>
        <circle cx="200" cy="248" r="28" fill="var(--orange)" role="img" aria-label="Vanilla flower and pods"/>
        <text font-family="Noto Sans JP,sans-serif" font-size="16" fill="var(--white)"><textPath href="#vBot" startOffset="50%" text-anchor="middle">バニラ　アイスクリーム - 500mL</textPath></text>
      </svg>
    </div>
    <div class="nz-badge" style="left:420px;top:118px;width:132px;height:132px;font-size:12px">
      <span>Your fresh taste</span>
      <span class="nz-badge__mark" role="img" aria-label="Fern leaf emblem" style="width:40px;height:40px"></span>
      <span>of New Zealand</span>
    </div>
    <p class="claim" style="left:108px;top:698px;color:var(--aqua);font-size:25px">
      <span class="claim__brand">Merrow's</span> uses <span class="claim__pct" style="font-size:30px">100%</span><br>fresh milk &amp; cream
    </p>
  </section>

  <!-- Lid label -->
  <section class="lid">
    <div class="milk-splash" role="img" aria-label="Splash of fresh milk" style="height:110px;background:linear-gradient(180deg,rgba(255,255,255,0) 0%,var(--white) 60%)"></div>
    <div class="seal" style="left:20px;top:12px;width:245px;height:245px">
      <svg viewBox="0 0 400 400">
        <g fill="var(--navy)">
          <rect x="58.6" y="58.6" width="282.8" height="282.8"/>
          <rect x="58.6" y="58.6" width="282.8" height="282.8" transform="rotate(11.25 200 200)"/>
          <rect x="58.6" y="58.6" width="282.8" height="282.8" transform="rotate(22.5 200 200)"/>
          <rect x="58.6" y="58.6" width="282.8" height="282.8" transform="rotate(33.75 200 200)"/>
          <rect x="58.6" y="58.6" width="282.8" height="282.8" transform="rotate(45 200 200)"/>
          <rect x="58.6" y="58.6" width="282.8" height="282.8" transform="rotate(56.25 200 200)"/>
          <rect x="58.6" y="58.6" width="282.8" height="282.8" transform="rotate(67.5 200 200)"/>
          <rect x="58.6" y="58.6" width="282.8" height="282.8" transform="rotate(78.75 200 200)"/>
        </g>
        <circle cx="200" cy="200" r="165" fill="none" stroke="var(--white)" stroke-width="3"/>
        <defs>
          <path id="lTop" d="M50,200 A150,150 0 0 1 350,200"/>
          <path id="lBot" d="M60,200 A140,140 0 0 0 340,200"/>
          <path id="lMid" d="M75,212 Q200,165 325,212"/>
        </defs>
        <text font-family="Open Sans,sans-serif" font-weight="700" font-size="17" fill="var(--white)"><textPath href="#lTop" startOffset="50%" text-anchor="middle">Vanilla Ice Cream - 500mL</textPath></text>
        <text x="200" y="162" text-anchor="middle" font-family="Open Sans,sans-serif" font-weight="700" font-size="48" fill="var(--white)">Merrow's</text>
        <text font-family="Open Sans,sans-serif" font-weight="700" font-size="18" fill="var(--white)"><textPath href="#lMid" startOffset="50%" text-anchor="middle">High Quality Ice Cream</textPath></text>
        <circle cx="200" cy="248" r="28" fill="var(--orange)" role="img" aria-label="Vanilla flower and pods"/>
        <text font-family="Noto Sans JP,sans-serif" font-size="16" fill="var(--white)"><textPath href="#lBot" startOffset="50%" text-anchor="middle">バニラ　アイスクリーム - 500mL</textPath></text>
      </svg>
    </div>
    <div class="nz-badge" style="left:232px;top:112px;width:86px;height:86px;font-size:8px">
      <span>Your fresh taste</span>
      <span class="nz-badge__mark" role="img" aria-label="Fern leaf emblem" style="width:26px;height:26px"></span>
      <span>of New Zealand</span>
    </div>
    <p class="claim" style="left:72px;top:262px;color:var(--navy);font-size:11px">
      <span class="claim__brand">Merrow's</span> uses <span class="claim__pct" style="font-size:14px">100%</span><br>fresh milk &amp; cream
    </p>
  </section>

  <!-- Strawberry 500mL label -->
  <section class="label label--strawberry">
    <div class="milk-splash" role="img" aria-label="Splash of fresh milk" style="height:110px"></div>
    <div class="seal" style="left:30px;top:70px;width:255px;height:255px">
      <svg viewBox="0 0 400 400">
        <g fill="var(--red)">
          <rect x="58.6" y="58.6" width="282.8" height="282.8"/>
          <rect x="58.6" y="58.6" width="282.8" height="282.8" transform="rotate(11.25 200 200)"/>
          <rect x="58.6" y="58.6" width="282.8" height="282.8" transform="rotate(22.5 200 200)"/>
          <rect x="58.6" y="58.6" width="282.8" height="282.8" transform="rotate(33.75 200 200)"/>
          <rect x="58.6" y="58.6" width="282.8" height="282.8" transform="rotate(45 200 200)"/>
          <rect x="58.6" y="58.6" width="282.8" height="282.8" transform="rotate(56.25 200 200)"/>
          <rect x="58.6" y="58.6" width="282.8" height="282.8" transform="rotate(67.5 200 200)"/>
          <rect x="58.6" y="58.6" width="282.8" height="282.8" transform="rotate(78.75 200 200)"/>
        </g>
        <circle cx="200" cy="200" r="165" fill="none" stroke="var(--white)" stroke-width="3"/>
        <defs>
          <path id="sTop" d="M50,200 A150,150 0 0 1 350,200"/>
          <path id="sBot" d="M60,200 A140,140 0 0 0 340,200"/>
          <path id="sMid" d="M75,212 Q200,165 325,212"/>
        </defs>
        <text font-family="Open Sans,sans-serif" font-weight="700" font-size="16" fill="var(--white)"><textPath href="#sTop" startOffset="50%" text-anchor="middle">Strawberry Ice Cream - 500mL</textPath></text>
        <text x="200" y="162" text-anchor="middle" font-family="Open Sans,sans-serif" font-weight="700" font-size="48" fill="var(--white)">Merrow's</text>
        <text font-family="Open Sans,sans-serif" font-weight="700" font-size="18" fill="var(--white)"><textPath href="#sMid" startOffset="50%" text-anchor="middle">High Quality Ice Cream</textPath></text>
        <circle cx="200" cy="248" r="28" fill="var(--orange)" role="img" aria-label="Fresh strawberry"/>
        <text font-family="Noto Sans JP,sans-serif" font-size="15" fill="var(--white)"><textPath href="#sBot" startOffset="50%" text-anchor="middle">ストロベリー アイスクリーム - 500mL</textPath></text>
      </svg>
    </div>
    <div class="nz-badge" style="left:228px;top:38px;width:80px;height:80px;font-size:7.5px">
      <span>Your fresh taste</span>
      <span class="nz-badge__mark" role="img" aria-label="Fern leaf emblem" style="width:24px;height:24px"></span>
      <span>of New Zealand</span>
    </div>
    <p class="claim" style="left:50px;top:362px;color:var(--red);font-size:12px">
      <span class="claim__brand">Merrow's</span> uses <span class="claim__pct" style="font-size:15px">100%</span><br>fresh milk &amp; cream
    </p>
  </section>

</main>
</body>
</html>
```